We need 3 A2 posters similar look but different enough to be eye catching when changed.

We are a healthcare centre that requires 3 A2 posters - simple, similar but different background colours. These posters will be used within our business to promote services we provide to our clients.

The design should include our logo(attached), a large header and a large section in the middle of the poster to promote the event. We need a blank text box (which WE can insert text to advertise), and 1 image to advertise the event. Please note, we do not need you to choose an image we simply would like you to place a demo to give us an idea of where it should sit.

We want to use the bubble design (attached) as a background and the company colours pink, orange and blue - as on our website. Attached is a copy of our logo and background bubble effect. You can also refer to our website - www.tallowparkwellness.com.au for more inspiration.

Just to reiterate, these posters should be simple, different but have a uniform feel. They should have an empty middle section that can be edited to add text and a space for an eye catching title and matching image.

Our services include Chiropractic, Podiatry, Nutrition, Massage, Yoga, Pilates and Specialised rehabilitation classes.

Reason: Hi designers, I know we are all busy but I really need more designs from the designers I invited to this project and look forward to receiving more designs. Any questions please let me know. Regards, Marnie

Reason: Hi all Increased the budget Regards Marnie

Corporate Sydney City office workers

Healthcare

• logo and company colours
section in the middles that can be edited to add text
Space allocated for image placement
Catchy title/header

```html
<!DOCTYPE html>
<html lang="en">
<head>
<meta charset="utf-8">
<title>Tallow Park Wellness – Poster</title>
<link rel="stylesheet" href="https://fonts.googleapis.com/css2?family=Poppins:wght@600;700&display=swap">
<style>
  :root {
    --pink: #bd2fe2;
    --orange: #d68d45;
    --blue: #5f7ff5;
    --sand: #e8caa2;
    --white: #ffffff;
    --page: #ffffff;
    --edge: #a9a9a9;
  }
  html, body {
    margin: 0;
    padding: 0;
    width: 976px;
    height: 1200px;
    overflow: hidden;
    background: var(--page);
  }
  .poster {
    position: absolute;
    left: 101px;
    top: 57px;
    width: 781px;
    height: 1105px;
    transform: scale(0.976);
    transform-origin: top left;
    overflow: hidden;
    outline: 1px solid var(--edge);
    font-family: "Poppins", sans-serif;
  }
  .bubble-backdrop {
    position: absolute;
    inset: 0;
    background:
      radial-gradient(circle at 12% 35%, rgba(233,170,170,0.55) 0, rgba(233,170,170,0) 22%),
      radial-gradient(circle at 90% 60%, rgba(233,170,175,0.5) 0, rgba(233,170,175,0) 20%),
      radial-gradient(circle at 8% 85%, rgba(233,170,170,0.5) 0, rgba(233,170,170,0) 18%),
      radial-gradient(circle at 95% 10%, rgba(233,175,170,0.45) 0, rgba(233,175,170,0) 15%),
      linear-gradient(180deg, var(--sand), #e6c7a4);
  }
  .top-band {
    position: absolute;
    left: 0; top: 0;
    width: 781px;
    height: 74px;
    background: var(--blue);
  }
  .brand {
    position: absolute;
    left: 22px;
    top: 22px;
    display: flex;
    align-items: center;
    gap: 12px;
  }
  .brand-dot {
    width: 18px;
    height: 18px;
    border-radius: 50%;
    background: var(--white);
  }
  .brand-name {
    margin: 0;
    font-weight: 600;
    font-size: 26px;
    line-height: 36px;
    color: var(--white);
  }
  .header-tab {
    position: absolute;
    left: 53px;
    top: 74px;
    width: 660px;
    height: 93px;
    background: var(--orange);
    border-radius: 0 0 12px 12px;
    box-sizing: border-box;
    padding-right: 24px;
    text-align: right;
  }
  .header-title {
    margin: 0;
    font-weight: 700;
    font-size: 41px;
    line-height: 93px;
    color: var(--white);
    letter-spacing: 0.3px;
  }
  .content-box {
    position: absolute;
    left: 55px;
    top: 413px;
    width: 672px;
    height: 649px;
    box-sizing: border-box;
    background: var(--white);
    border: 8px solid var(--orange);
    border-radius: 20px;
  }
  .image-slot {
    position: absolute;
    left: 221px;
    top: 205px;
    width: 540px;
    height: 255px;
    box-sizing: border-box;
    border: 4px solid var(--orange);
    border-radius: 14px;
    background: linear-gradient(160deg, #fbfaf7 0%, #f3efe6 55%, #e7dccb 100%);
    box-shadow: 0 18px 30px rgba(120,170,180,0.28);
  }
  .welcome-copy {
    position: absolute;
    left: 87px;
    top: 522px;
    width: 610px;
    margin: 0;
    font-weight: 600;
    font-size: 20px;
    line-height: 28.5px;
    color: var(--orange);
  }
  .welcome-copy + .welcome-copy { top: 692px; }
  .foot-bar {
    position: absolute;
    left: 0;
    top: 1087px;
    width: 781px;
    height: 18px;
    display: flex;
  }
  .foot-bar .seg-blue { width: 541px; background: var(--blue); }
  .foot-bar .seg-orange { width: 72px; background: var(--orange); }
  .foot-bar .seg-pink { flex: 1; background: var(--pink); }
</style>
</head>
<body>
  <main class="poster">
    <div class="bubble-backdrop" role="img" aria-label="Soft bubble pattern of overlapping rounded squares in sand and rose tones"></div>

    <header>
      <div class="top-band"></div>
      <div class="brand">
        <span class="brand-dot"></span>
        <p class="brand-name">Tallow Park Wellness</p>
      </div>
      <div class="header-tab">
        <h1 class="header-title">Header text space</h1>
      </div>
    </header>

    <section class="content-box"></section>
    <div class="image-slot" role="img" aria-label="Event photo placeholder: a client relaxing on a massage table in a bright spa room"></div>

    <p class="welcome-copy">Welcome to Tallow Park Wellness. Our goal is to<br>achieve the best possible health outcome for our<br>patients. Our unique combination of therapies,<br>structural correction and individualised exercise<br>programs is what sets us apart.</p>
    <p class="welcome-copy">At anytime, if you have a health condition, even if<br>you feel it is not something we could help you with,<br>contact us and we will find the right solution for you.<br>We are here for the health of our community"</p>

    <footer class="foot-bar">
      <span class="seg-blue"></span>
      <span class="seg-orange"></span>
      <span class="seg-pink"></span>
    </footer>
  </main>
</body>
</html>
```